Business Card for a Floral & Decorating Business

I would like to take my current logo and create a better business card. I am looking for elegance as I am a florist and event decorator. My logo has multiple colour options. I like colours like green, purple, pink and orange, I think I would like a white card, open to black back ground. I want it to feel elegant and romantic. I like metallic lettering that maybe is indented in the paper, I also like glossy paper. I have a full logo already as well as a badge. I have attached both in multiple colours.m

Target Market(s)

Weddings, special events, floral customers

Industry/Entity Type

Floral and decorating

Contact Information for Business Card

Phone number, email, instagram, facebook, title, name, logo

Font styles to use
Script

Requirements
Nice to have
• Elegant

```html
<!DOCTYPE html>
<html lang="en">
<head>
<meta charset="utf-8">
<title>Maren Holloway Decorating &amp; Florals – Business Card</title>
<link rel="stylesheet" href="https://fonts.googleapis.com/css2?family=Cormorant+Garamond:wght@400;500&family=Roboto:wght@400;500&family=Cinzel:wght@400&display=swap">
<style>
  :root {
    --backdrop: #e9e4dc;
    --card-white: #ffffff;
    --sage: #6f8a72;
    --sage-deep: #5f7862;
    --sage-back: #718a74;
    --sage-light: #bdd3bc;
    --bronze: #9a7248;
    --ink: #2f2f2f;
    --rule: #8a8a8a;
  }
  * { margin: 0; padding: 0; box-sizing: border-box; }
  html, body { width: 900px; height: 1200px; overflow: hidden; }
  body { background: var(--backdrop); position: relative; font-family: "Roboto", Arial, sans-serif; }

  .card {
    position: absolute;
    border-radius: 40px;
    box-shadow: 0 6px 14px rgba(0,0,0,0.28);
  }
  .card--front { left: 68px; top: 130px; width: 775px; height: 442px; background: var(--card-white); }
  .card--back  { left: 66px; top: 635px; width: 780px; height: 443px; background: var(--sage-back); }

  .brand-mark { position: absolute; border-radius: 50%; }
  .card--front .brand-mark { left: 362px; top: 45px; width: 56px; height: 56px; background: var(--sage); }
  .card--back .brand-mark { left: 344px; top: 48px; width: 110px; height: 110px; background: var(--sage-light); }

  .brand-name {
    position: absolute; left: 0; width: 100%; text-align: center;
    font-family: "Cormorant Garamond", Georgia, serif; font-weight: 400;
  }
  .card--front .brand-name { top: 118px; font-size: 60px; color: var(--sage); line-height: 1; }
  .card--back .brand-name { top: 195px; font-size: 104px; color: var(--sage-light); line-height: 1; }

  .brand-tagline {
    position: absolute; left: 0; width: 100%; text-align: center;
    font-family: "Cinzel", Georgia, serif;
  }
  .card--front .brand-tagline { top: 205px; font-size: 12.5px; letter-spacing: 3px; color: var(--bronze); }
  .card--back .brand-tagline { top: 337px; font-size: 21px; letter-spacing: 6px; color: var(--sage-light); }

  .holder { position: absolute; right: 411px; top: 266px; text-align: right; }
  .holder__name { font-size: 34px; font-weight: 500; color: var(--sage); line-height: 1.1; }
  .holder__title { font-size: 19px; color: var(--ink); margin-top: 2px; }

  .divider { position: absolute; left: 387px; top: 255px; width: 2px; height: 88px; background: var(--rule); }

  .contacts { position: absolute; left: 405px; top: 260px; list-style: none; }
  .contacts li { display: flex; align-items: center; height: 25px; font-size: 16px; color: var(--ink); }
  .contacts li:first-child { font-size: 17px; }
  .contacts svg { width: 18px; height: 18px; margin-right: 12px; fill: none; stroke: #555; stroke-width: 1.6; }

  .services {
    position: absolute; left: 0; width: 100%; top: 391px; text-align: center;
    font-size: 13px; letter-spacing: 2.6px; color: var(--bronze);
  }
  .services .dot { display: inline-block; width: 7px; height: 7px; border-radius: 50%; background: var(--bronze); margin: 0 10px; vertical-align: 2px; }
</style>
</head>
<body>
  <section class="card card--front">
    <div class="brand-mark"></div>
    <div class="brand-name">Maren Holloway</div>
    <div class="brand-tagline">DECORATING &amp; FLORALS.</div>

    <div class="holder">
      <div class="holder__name">Elliot Fairbanks</div>
      <div class="holder__title">Owner</div>
    </div>
    <div class="divider"></div>
    <ul class="contacts">
      <li><svg viewBox="0 0 24 24"><path d="M6 3l3 4-2 2c1 3 4 6 7 7l2-2 4 3-2 3C11 20 4 13 3 5z"/></svg>555-014-2290</li>
      <li><svg viewBox="0 0 24 24"><rect x="3" y="6" width="18" height="12"/><path d="M3 6l9 7 9-7"/></svg>hello@marenhollowayfloral.com</li>
      <li><svg viewBox="0 0 24 24"><circle cx="12" cy="12" r="9"/><path d="M3 12h18M12 3c3 3 3 15 0 18M12 3c-3 3-3 15 0 18"/></svg>www.marenhollowayevents.com</li>
    </ul>

    <div class="services">WEDDINGS<span class="dot"></span>SPECIAL EVENTS<span class="dot"></span>FLORAL CUSTOMERS</div>
  </section>

  <section class="card card--back">
    <div class="brand-mark"></div>
    <div class="brand-name">Maren Holloway</div>
    <div class="brand-tagline">DECORATING &amp; FLORALS.</div>
  </section>
</body>
</html>
```